KRV Business Cards

We are a local commercial development company based in Silicon Valley and we would like a new business card. I've attached a copy of our company brochure to give a flavor of what we do, our logo, info company colors/graphics, and our current business card. We don't necessarily need a crazy makeover, but would like something that feels a little bit more "fresh" and modern (we've had the same business card design for 15+ years), but still in keeping with our overall brand -- clean, high-quality, modern but timeless. Would like to add our website to the info on the card (www.velmara.com) and would like the flexibility for some folks to have an efax number listed and some not to have that included (without it looking like there is a hole).

```html
<!DOCTYPE html>
<html lang="en">
<head>
<meta charset="utf-8">
<title>KRV Business Cards</title>
<link rel="stylesheet" href="https://fonts.googleapis.com/css2?family=Crimson+Text:ital@1&family=Montserrat:wght@400;600&display=swap">
<style>
  :root {
    --stage: #eceded;
    --paper: #ffffff;
    --navy: #334e66;
    --navy-line: #5a7389;
    --grey-band: #bcbcbc;
    --ink: #334e66;
    --ink-soft: #6b7a88;
  }
  * { margin: 0; padding: 0; box-sizing: border-box; }
  html, body { width: 1200px; height: 900px; overflow: hidden; background: var(--stage); }
  .board { position: relative; width: 1200px; height: 900px; }

  .card { position: absolute; width: 514px; height: 296px; background: var(--paper); overflow: hidden; }
  .card--navy { background: var(--navy); }
  .pos-front-a { left: 73px; top: 138px; }
  .pos-back-a  { left: 615px; top: 138px; }
  .pos-front-b { left: 73px; top: 463px; }
  .pos-back-b  { left: 615px; top: 463px; }

  .company-name {
    position: absolute; font-family: "Montserrat", sans-serif; font-weight: 400;
    color: var(--paper); font-size: 17px; line-height: 1.35; letter-spacing: 0.5px;
  }
  .brand-block { position: absolute; background: var(--navy); }

  .tagline { position: absolute; font-family: "Crimson Text", serif; font-style: italic; color: var(--ink); }

  .band-grey { position: absolute; left: 0; width: 100%; background: var(--grey-band); }

  .contact { position: absolute; font-family: "Montserrat", sans-serif; color: var(--ink); font-size: 13px; line-height: 1.32; }
  .contact .name { font-weight: 600; font-size: 18px; line-height: 1.1; }
  .contact .role { font-weight: 600; font-size: 12px; color: var(--ink-soft); margin-bottom: 18px; }
  .contact .label { color: var(--ink-soft); }
  .contact .web { font-weight: 600; }
  .gap { height: 10px; }
  .rule-v { position: absolute; width: 1.5px; background: var(--navy-line); }
  .rule-h { position: absolute; height: 1.5px; background: var(--navy-line); }
</style>
</head>
<body>
<main class="board">

  <section class="card card--navy pos-front-a">
    <div class="company-name" style="left:0; width:514px; top:125px; text-align:center; font-size:19px;">KRV<br>Development Co.</div>
  </section>

  <section class="card pos-back-a">
    <div class="band-grey" style="top:0; height:36px;"></div>
    <div class="brand-block" style="left:0; top:36px; width:232px; height:113px;">
      <div class="company-name" style="left:0; width:232px; top:34px; text-align:center;">KRV<br>Development Co.</div>
    </div>
    <div class="tagline" style="left:304px; top:50px; font-size:25px; line-height:1.1;">Spaces Built<br>for Lasting<br>Work</div>
    <div class="band-grey" style="top:149px; height:5px;"></div>
    <div class="contact" style="left:39px; top:184px;">
      <div class="name">Dana L. Whitcomb</div>
      <div class="role">Partner</div>
      <div><span class="label">direct</span>&nbsp; 650 555 0148</div>
      <div><span class="label">email</span>&nbsp; dana@velmara.com</div>
    </div>
    <div class="rule-v" style="left:288px; top:179px; height:97px;"></div>
    <div class="contact" style="left:306px; top:184px;">
      <div>212 Larkin Street</div>
      <div>Alder Heights, CA 95512</div>
      <div class="gap"></div>
      <div><span class="label">tel</span>&nbsp; 650 555 0190</div>
      <div><span class="label">fax</span> 650 555 0162</div>
      <div class="web">www.velmara.com</div>
    </div>
  </section>

  <section class="card pos-front-b">
    <div class="brand-block" style="left:151px; top:92px; width:209px; height:114px;">
      <div class="company-name" style="left:0; width:209px; top:34px; text-align:center;">KRV<br>Development Co.</div>
    </div>
  </section>

  <section class="card pos-back-b">
    <div class="brand-block" style="left:0; top:45px; width:232px; height:208px;">
      <div class="company-name" style="left:0; width:232px; top:34px; text-align:center;">KRV<br>Development Co.</div>
      <div class="rule-h" style="left:40px; top:111px; width:152px;"></div>
      <div class="tagline" style="left:0; width:232px; top:130px; font-size:15px; line-height:1.4; text-align:center; color:var(--paper);">Spaces Built<br>for Lasting Work</div>
    </div>
    <div class="contact" style="left:271px; top:52px;">
      <div class="name">Dana L. Whitcomb</div>
      <div class="role" style="margin-bottom:10px;">Partner</div>
      <div><span class="label">direct</span>&nbsp; 650 555 0148</div>
      <div><span class="label">email</span>&nbsp; dana@velmara.com</div>
    </div>
    <div class="rule-h" style="left:271px; top:138px; width:203px;"></div>
    <div class="contact" style="left:271px; top:155px;">
      <div>212 Larkin Street</div>
      <div>Alder Heights, CA 95512</div>
      <div class="gap"></div>
      <div><span class="label">tel</span>&nbsp; 650 555 0190</div>
      <div><span class="label">fax</span> 650 555 0162</div>
      <div class="web">www.velmara.com</div>
    </div>
  </section>

</main>
</body>
</html>
```